Corvanto Card

The logo is the Spanish flag colors I want a vibrant eye catching design with the yellow / red colors over either Navy or white background or black even ,
Would like a 2D feel to the logo with another lighter color logo under it look ,

Contact Information for Business Card

Corvanto Flooring
Tobias Renwick
Main Number
Cell Number
Fax Number

Website on the side of the card somewhere

Font styles to use
Sans Serif

Colors
ec1f27
ffc214

Requirements
Must have
• 2 logos feel one is bolder and the other one underneath very light

```html
<!DOCTYPE html>
<html lang="en">
<head>
<meta charset="utf-8">
<title>Corvanto Card</title>
<link rel="stylesheet" href="https://fonts.googleapis.com/css2?family=Open+Sans:wght@400;700&family=Montserrat:wght@500&display=swap">
<style>
  :root {
    --scene-bg: #3a3a3a;
    --card-black: #1f1f1f;
    --card-pattern: #191919;
    --tone-faint: #2a2a2a;
    --brand-red: #ec1f27;
    --brand-yellow: #ffc214;
    --edge-red: #b3141b;
    --text-light: #f2f2f2;
  }
  * { box-sizing: border-box; margin: 0; padding: 0; }
  html, body {
    width: 1200px; height: 801px; overflow: hidden;
    background: var(--scene-bg);
    font-family: "Open Sans", Arial, sans-serif;
  }
  .sheet {
    position: relative; width: 1200px; height: 801px;
    display: flex; align-items: center; justify-content: center; gap: 60px;
  }
  .card {
    position: relative; width: 520px; height: 297px;
    background: var(--card-black);
    border: 2px solid var(--edge-red);
    box-shadow: 0 14px 30px rgba(0,0,0,.35);
    overflow: hidden;
  }
  /* front */
  .brand-block {
    position: absolute; left: 28px; top: 0; width: 222px; height: 100%;
    display: flex; align-items: center; justify-content: center; gap: 10px;
  }
  .brand-square { width: 16px; height: 16px; background: var(--brand-red); flex: none; }
  .brand-name {
    font-family: "Montserrat", Arial, sans-serif; font-weight: 500;
    color: var(--brand-yellow); font-size: 17px; letter-spacing: 3px;
    text-transform: uppercase; line-height: 1.3;
  }
  .divider {
    position: absolute; left: 268px; top: 62px; width: 1.5px; height: 172px;
    background: var(--brand-yellow);
  }
  .contact {
    position: absolute; left: 288px; top: 56px; color: var(--text-light);
    font-size: 11.5px; line-height: 1.45;
  }
  .contact .person {
    color: var(--brand-yellow); font-weight: 700; font-size: 17px;
    text-transform: uppercase; letter-spacing: .3px; line-height: 1.2;
  }
  .contact .role { margin-bottom: 10px; }
  .contact .address { margin-bottom: 10px; }
  .contact-list { list-style: none; }
  .contact-list li { display: flex; align-items: center; gap: 7px; }
  .contact-list svg { width: 10px; height: 10px; fill: var(--brand-red); flex: none; }
  /* back */
  .pattern-field {
    position: absolute; inset: 0;
    background: radial-gradient(circle at 60% 40%, #232323 0%, var(--card-pattern) 75%);
  }
  .faint-wordmark {
    position: absolute; left: 34px; top: 44px;
    font-family: "Montserrat", Arial, sans-serif; font-weight: 500;
    color: var(--tone-faint); font-size: 46px; letter-spacing: 8px;
    text-transform: uppercase; line-height: 1.2;
  }
  .back-brand {
    position: absolute; right: 34px; bottom: 40px;
    display: flex; align-items: center; gap: 8px;
  }
  .back-brand .brand-name { font-size: 12px; letter-spacing: 2px; }
  .back-brand .brand-square { width: 11px; height: 11px; }
</style>
</head>
<body>
<main class="sheet">
  <section class="card card-front">
    <div class="brand-block">
      <span class="brand-square"></span>
      <span class="brand-name">Corvanto<br>Flooring</span>
    </div>
    <div class="divider"></div>
    <div class="contact">
      <p class="person">Tobias Renwick</p>
      <p class="role">President</p>
      <p class="address">3187 Larkspur Bay Road<br>Port Elwin CA 90417</p>
      <ul class="contact-list">
        <li><svg viewBox="0 0 10 10"><path d="M2 0l2 2-1 1.5c.7 1.5 2 2.8 3.5 3.5L8 6l2 2-1.5 2C4 10 0 6 0 1.5z"/></svg>555-018-2740</li>
        <li><svg viewBox="0 0 10 10"><path d="M2.5 0h5v10h-5zM3.5 1v7h3V1z"/></svg>555-018-2740</li>
        <li><svg viewBox="0 0 10 10"><path d="M2.5 0h5v3h-5zM0 3.5h10v4.5H8V10H2V8H0zM3 6.5v2.5h4V6.5z"/></svg>555-018-2740</li>
        <li><svg viewBox="0 0 10 10"><path d="M0 2h10v6H0zM1 3l4 3 4-3v-.2H1z"/></svg>info@corvantoflooring.com</li>
        <li><svg viewBox="0 0 10 10"><circle cx="5" cy="5" r="5"/></svg>www.corvantoflooring.com</li>
      </ul>
    </div>
  </section>
  <section class="card card-back">
    <div class="pattern-field" role="img" aria-label="Tonal embossed repeat pattern of the brand mark across the black card back"></div>
    <p class="faint-wordmark" aria-hidden="true">Corvanto<br>Flooring</p>
    <div class="back-brand">
      <span class="brand-square"></span>
      <span class="brand-name">Corvanto Flooring</span>
    </div>
  </section>
</main>
</body>
</html>
```